Modern Corvane Tree Care Website

I need a website for a full service Tree Care company. The company provides tree pruning, tree removal, tree preservation, emergency services, stump grinding, and emergency tree services.

Target Market(s)

Customers that need tree services

Industry/Entity Type

Landscaping, Tree Services

Coding

Coded - Design and coding required

Number of Pages Required

5+ page

Font styles to use
Sans Serif

Requirements
Must have
• Good clean design that showcases the services the company provides.
Nice to have
• Services page; contact form, blog, home page, about page

```html
<!DOCTYPE html>
<html lang="en">
<head>
<meta charset="utf-8">
<title>Corvane Tree Care</title>
<link rel="stylesheet" href="https://fonts.googleapis.com/css2?family=Libre+Baskerville&family=Roboto:wght@400;500;700&display=swap">
<style>
:root{
  --green:#7cc242;
  --green-dark:#5fa32c;
  --orange:#f7a733;
  --heading:#5d6a72;
  --text:#6b6b6b;
  --ink:#222;
  --footer:#2e4a2b;
  --white:#fff;
}
*{margin:0;padding:0;box-sizing:border-box}
html,body{width:1200px;height:4104px;overflow:hidden;background:var(--white)}
body{font-family:"Roboto",sans-serif;color:var(--text);position:relative}
.serif{font-family:"Libre Baskerville",serif;font-weight:400}
.abs{position:absolute}
.btn{position:absolute;background:var(--orange);color:var(--white);border-radius:24px;font:700 12px "Roboto",sans-serif;display:flex;align-items:center;justify-content:center;letter-spacing:.2px}

/* header */
.site-header{position:absolute;left:0;top:0;width:1200px;height:80px;background:var(--white);z-index:5}
.brand{position:absolute;left:142px;top:20px;display:flex;align-items:center;gap:10px}
.brand-mark{width:34px;height:34px;background:var(--green);flex:none}
.brand-name{font:700 16px "Roboto",sans-serif;color:var(--green);line-height:1.1;text-transform:uppercase;letter-spacing:.5px;white-space:nowrap}
.nav a{position:absolute;top:34px;font:400 12px "Roboto",sans-serif;color:var(--ink);text-decoration:none}
.nav a.active{color:var(--green)}
.social{position:absolute;top:27px;width:26px;height:26px;border:1.5px solid var(--orange);border-radius:50%}
.head-divider{position:absolute;left:851px;top:16px;width:2px;height:48px;background:var(--orange)}
.call-label{position:absolute;left:920px;top:21px;font:400 12px "Roboto",sans-serif;color:var(--ink)}
.call-number{position:absolute;left:920px;top:38px;font:700 18px "Roboto",sans-serif;color:var(--ink)}

/* hero */
.hero{position:absolute;left:0;top:80px;width:1200px;height:700px;z-index:2}
.hero-title{position:absolute;left:142px;top:160px;font-size:54px;line-height:72px;color:var(--white);white-space:nowrap}
.slider-dot{position:absolute;top:475px;width:38px;height:38px;border-radius:50%;background:var(--white)}
.quote{position:absolute;left:695px;top:71px;width:362px;height:439px;background:var(--white)}
.quote h2{position:absolute;left:0;width:100%;top:28px;text-align:center;font-size:36px;color:var(--heading)}
.field{position:absolute;left:24px;width:312px;border:1px solid #ddd;font:400 12px "Roboto",sans-serif;color:#777;padding:12px 14px}

/* services */
.services-bg{position:absolute;left:0;top:0;z-index:0}
.section-title{position:absolute;left:0;width:1200px;text-align:center;font-size:36px}
.card-ring{position:absolute;width:270px;height:462px;background:rgba(255,255,255,.35);clip-path:polygon(50% 0,100% 10%,100% 90%,50% 100%,0 90%,0 10%)}
.card{position:absolute;top:961px;width:260px;height:450px;background:var(--white);clip-path:polygon(50% 0,100% 10%,100% 90%,50% 100%,0 90%,0 10%);z-index:1}
.card-photo{position:absolute;left:11px;top:14px;width:238px;height:236px;clip-path:polygon(50% 0,100% 22%,100% 78%,50% 100%,0 78%,0 22%)}
.card h3{position:absolute;top:270px;width:100%;text-align:center;font:400 22px "Roboto",sans-serif;color:var(--ink)}
.card p{position:absolute;top:306px;left:30px;width:200px;text-align:center;font-size:13px;line-height:20px;color:var(--text)}
.card-more{position:absolute;left:109px;top:380px;width:42px;height:42px;background:var(--orange);clip-path:polygon(50% 0,100% 25%,100% 75%,50% 100%,0 75%,0 25%);display:flex;align-items:center;justify-content:center}
.card-more svg{width:12px;height:12px}

/* about */
.about-frame{position:absolute;left:235px;top:1800px;width:367px;height:307px;border:5px solid var(--green)}
.about-photo{position:absolute;left:143px;top:1725px;width:436px;height:358px;background:linear-gradient(135deg,#5f7d3a,#8c7b5d 55%,#3d3b36)}
.years{position:absolute;left:121px;top:1690px;width:204px;height:90px;background:var(--green);border:3px solid var(--white);color:var(--white)}
.years b{position:absolute;left:16px;top:14px;font:400 52px "Libre Baskerville",serif;line-height:1}
.years span{position:absolute;left:86px;top:24px;font:400 15px/22px "Roboto",sans-serif;text-transform:uppercase}
.about-title{position:absolute;left:638px;top:1736px;font-size:44px;color:var(--heading)}
.about-text{position:absolute;left:638px;top:1795px;width:416px;font-size:13px;line-height:19.9px;text-align:justify;color:var(--text)}

/* why choose */
.why-hex{position:absolute;width:223px;height:240px;background:rgba(255,255,255,.35);clip-path:polygon(50% 0,100% 25%,100% 75%,50% 100%,0 75%,0 25%)}
.why-hex .inner{position:absolute;left:9px;top:10px;width:205px;height:220px;background:var(--white);clip-path:polygon(50% 0,100% 25%,100% 75%,50% 100%,0 75%,0 25%)}
.why-hex svg{position:absolute;left:80px;top:60px;width:62px;height:62px}
.why-hex .label{position:absolute;left:20px;top:145px;width:183px;text-align:center;font:500 14px/24px "Roboto",sans-serif;color:var(--ink)}

/* gallery */
.gallery-tile{position:absolute}

/* footer */
.footer-brand{position:absolute;left:191px;top:3832px;display:flex;align-items:center;gap:12px}
.footer-brand .brand-mark{width:48px;height:48px}
.footer-brand .brand-name{font-size:22px;line-height:1.15}
.foot-h{position:absolute;top:3832px;font-size:16px;color:var(--white);font-weight:700}
.foot-list{position:absolute;top:3874px;list-style:none;font-size:12px;line-height:20px;color:var(--white)}
.contact-item{position:absolute;left:816px;display:flex;align-items:flex-start;gap:12px;font-size:12px;line-height:20px;color:var(--white)}
.contact-icon{width:28px;height:28px;border-radius:50%;background:var(--green);display:flex;align-items:center;justify-content:center;flex:none}
.contact-icon svg{width:13px;height:13px}
.foot-line{position:absolute;left:200px;top:4049px;width:800px;height:1px;background:rgba(255,255,255,.18)}
.copyright{position:absolute;left:0;top:4067px;width:1200px;text-align:center;font-size:12px;color:var(--white)}
</style>
</head>
<body>

<!-- background bands -->
<svg class="services-bg" width="1200" height="4104" viewBox="0 0 1200 4104" aria-hidden="true">
  <defs>
    <linearGradient id="whyGrad" x1="0" y1="0" x2="1" y2="1">
      <stop offset="0" stop-color="#6fb33a"/>
      <stop offset=".5" stop-color="#8cc84e"/>
      <stop offset="1" stop-color="#72b53c"/>
    </linearGradient>
    <linearGradient id="footGrad" x1="0" y1="0" x2="0" y2="1">
      <stop offset="0" stop-color="#2b4628"/>
      <stop offset="1" stop-color="#314d2d"/>
    </linearGradient>
  </defs>
  <polygon points="0,640 1200,640 1200,1490 600,1590 0,1490" fill="#7cc242"/>
  <polygon points="0,2303 600,2203 1200,2303 1200,2885 600,2984 0,2885" fill="url(#whyGrad)"/>
  <polygon points="0,2303 600,2203 1200,2303 1200,2318 600,2222 0,2318" fill="#9bd160" opacity=".6"/>
  <polygon points="0,3800 600,3674 1200,3800" fill="#7cc242"/>
  <polygon points="0,3802 600,3703 1200,3802 1200,4104 0,4104" fill="url(#footGrad)"/>
</svg>

<!-- header -->
<header class="site-header">
  <div class="brand"><span class="brand-mark"></span><span class="brand-name">Corvane<br>Tree Care</span></div>
  <nav class="nav">
    <a class="active" style="left:352px">HOME</a>
    <a style="left:406px">SERVICES</a>
    <a style="left:483px">ABOUT US</a>
    <a style="left:561px">CONTACT US</a>
    <a style="left:655px">SHOWCASE</a>
  </nav>
  <span class="social" style="left:742px"></span>
  <span class="social" style="left:773px"></span>
  <span class="social" style="left:803px"></span>
  <span class="head-divider"></span>
  <svg class="abs" style="left:872px;top:20px" width="38" height="38" viewBox="0 0 24 24" fill="none" stroke="#f7a733" stroke-width="1.6" stroke-linecap="round" stroke-linejoin="round" aria-hidden="true">
    <path d="M5 3h3l2 5-2.5 1.5a11 11 0 0 0 7 7L16 14l5 2v3a2 2 0 0 1-2 2A16 16 0 0 1 3 5a2 2 0 0 1 2-2z"/>
    <path d="M15 3a6 6 0 0 1 6 6M15 6.5A2.5 2.5 0 0 1 17.5 9"/>
  </svg>
  <span class="call-label">CALL US :</span>
  <span class="call-number">+1 555 014 2290</span>
</header>

<!-- hero -->
<section class="hero">
  <svg class="abs" style="left:0;top:0" width="1200" height="700" viewBox="0 0 1200 700" role="img" aria-label="Photo of a large tree in a misty forest at sunrise">
    <defs>
      <linearGradient id="heroGrad" x1="0" y1="0" x2="1" y2=".4">
        <stop offset="0" stop-color="#2f3a1e"/>
        <stop offset=".35" stop-color="#5e5a3a"/>
        <stop offset=".6" stop-color="#c8b58c"/>
        <stop offset="1" stop-color="#6d6a2a"/>
      </linearGradient>
    </defs>
    <polygon points="260,621 600,693 940,621 600,660" fill="#f7a733"/>
    <polygon points="0,0 1200,0 1200,573 600,660 0,573" fill="url(#heroGrad)"/>
  </svg>
  <h1 class="hero-title serif">CORVANE TREE<br>CARE</h1>
  <div class="btn" style="left:142px;top:317px;width:154px;height:44px">GET STARTED</div>
  <span class="slider-dot" style="left:143px"></span>
  <span class="slider-dot" style="left:191px"></span>
  <svg class="abs" style="left:156px;top:488px" width="12" height="12" viewBox="0 0 12 12" fill="none" stroke="#333" stroke-width="1.5"><path d="M8 2 4 6l4 4"/></svg>
  <svg class="abs" style="left:204px;top:488px" width="12" height="12" viewBox="0 0 12 12" fill="none" stroke="#333" stroke-width="1.5"><path d="m4 2 4 4-4 4"/></svg>

  <form class="quote">
    <h2 class="serif">GET A QUOTE</h2>
    <div class="field" style="top:86px;height:40px">Name</div>
    <div class="field" style="top:134px;height:40px">Email</div>
    <div class="field" style="top:182px;height:40px">Phone</div>
    <div class="field" style="top:230px;height:121px">Message</div>
    <div class="btn" style="left:103px;top:359px;width:155px;height:45px">SUBMIT NOW</div>
  </form>
</section>

<!-- services -->
<h2 class="section-title serif" style="top:876px;color:var(--white)">OUR SERVICES</h2>

<svg class="abs" style="left:0;top:1164px" width="62" height="80" viewBox="0 0 62 80" aria-hidden="true"><polygon points="0,0 46,0 62,40 46,80 0,80" fill="#333"/><path d="M27 32 19 40l8 8" fill="none" stroke="#fff" stroke-width="2.4"/></svg>
<svg class="abs" style="left:1138px;top:1164px" width="62" height="80" viewBox="0 0 62 80" aria-hidden="true"><polygon points="62,0 16,0 0,40 16,80 62,80" fill="#333"/><path d="m35 32 8 8-8 8" fill="none" stroke="#fff" stroke-width="2.4"/></svg>

<div class="card-ring" style="left:161px;top:955px"></div>
<div class="card-ring" style="left:465px;top:955px"></div>
<div class="card-ring" style="left:770px;top:955px"></div>

<article class="card" style="left:166px">
  <div class="card-photo" role="img" aria-label="Photo of an arborist trimming branches with a chainsaw" style="background:linear-gradient(160deg,#7a5a4a,#b14a4a 50%,#3e3a34)"></div>
  <h3>Tree Trimming</h3>
  <p>Lorem ipsum dolor sit amet, consectetur adipiscing elit, sed do eiusmod tempor</p>
  <span class="card-more"><svg viewBox="0 0 12 12" fill="none" stroke="#fff" stroke-width="1.6"><path d="m2 3 3 3-3 3M7 3l3 3-3 3"/></svg></span>
</article>
<article class="card" style="left:470px">
  <div class="card-photo" role="img" aria-label="Photo of a worker beside a cut tree trunk near a house" style="background:linear-gradient(160deg,#9aa4ad,#7d7a58 50%,#a9895c)"></div>
  <h3>Tree Removal</h3>
  <p>Lorem ipsum dolor sit amet, consectetur adipiscing elit, sed do eiusmod tempor</p>
  <span class="card-more"><svg viewBox="0 0 12 12" fill="none" stroke="#fff" stroke-width="1.6"><path d="m2 3 3 3-3 3M7 3l3 3-3 3"/></svg></span>
</article>
<article class="card" style="left:775px">
  <div class="card-photo" role="img" aria-label="Photo of a climber working high in a tree" style="background:linear-gradient(160deg,#8fb0c8,#5d7d4a 55%,#3f5530)"></div>
  <h3>Tree Clearing</h3>
  <p>Lorem ipsum dolor sit amet, consectetur adipiscing elit, sed do eiusmod tempor</p>
  <span class="card-more"><svg viewBox="0 0 12 12" fill="none" stroke="#fff" stroke-width="1.6"><path d="m2 3 3 3-3 3M7 3l3 3-3 3"/></svg></span>
</article>

<!-- about -->
<div class="about-frame"></div>
<div class="about-photo" role="img" aria-label="Photo of an arborist cutting a tree trunk with a chainsaw"></div>
<div class="years"><b>20</b><span>Years<br>Experiences</span></div>
<h2 class="about-title serif">ABOUT US</h2>
<p class="about-text">Lorem ipsum dolor sit amet, consectetur adipiscing elit, sed do eiusmod tempor incididunt ut labore et dolore magna aliqua. Ut enim ad minim veniam, quis nostrud exercitation ullamco laboris nisi ut aliquip ex ea commodo consequat. Duis aute irure dolor in reprehenderit in voluptate velit esse cillum dolore eu fugiat nulla pariatur. Excepteur sint occaecat cupidatat non proident, sunt in culpa qui officia deserunt mollit anim id est laborum. Lorem ipsum dolor sit amet, consectetur adipiscing elit, sed do eiusmod tempor incididunt ut labore et dolore magna aliqua. Ut enim ad minim veniam, quis nostrud exercitation ullamco laboris nisi ut aliquip ex ea commodo consequat. Duis aute irure dolor in reprehenderit in voluptate velit esse cillum dolore eu fugiat nulla pariatur.</p>
<div class="btn" style="left:638px;top:2060px;width:154px;height:45px">LEARN MORE</div>

<!-- why choose us -->
<h2 class="section-title serif" style="top:2338px;color:var(--white);font-size:40px">WHY CHOOSE US</h2>

<div class="why-hex" style="left:136px;top:2405px"><div class="inner"></div>
  <svg viewBox="0 0 48 48" fill="none" stroke="#7cc242" stroke-width="1.8" stroke-linejoin="round"><path d="M14 6h18l6 6v30H14z"/><path d="M20 18h12M20 24h8"/><circle cx="32" cy="32" r="6"/><path d="m29 32 2 2 4-4"/><path d="M6 40h14M9 40v-6h8v6M13 34v-5"/></svg>
  <div class="label">Licensed and Insured</div></div>
<div class="why-hex" style="left:370px;top:2405px"><div class="inner"></div>
  <svg viewBox="0 0 48 48" fill="none" stroke="#7cc242" stroke-width="1.8" stroke-linejoin="round"><path d="M10 8h6l3 8-4 3a18 18 0 0 0 9 9l3-4 8 3v6a3 3 0 0 1-3 3A28 28 0 0 1 7 11a3 3 0 0 1 3-3z"/><circle cx="32" cy="16" r="10"/><path d="M32 10v6l4 3"/></svg>
  <div class="label">24-Hours Emergency<br>Services</div></div>
<div class="why-hex" style="left:605px;top:2405px"><div class="inner"></div>
  <svg viewBox="0 0 48 48" fill="none" stroke="#7cc242" stroke-width="1.8" stroke-linejoin="round"><circle cx="14" cy="8" r="4"/><path d="M8 42V18h12v24M14 28v14"/><circle cx="32" cy="30" r="10"/><path d="M35 25h-4a2 2 0 0 0 0 4h2a2 2 0 0 1 0 4h-4M32 23v2M32 33v2"/></svg>
  <div class="label">Locally Owned &amp;<br>Operated</div></div>
<div class="why-hex" style="left:839px;top:2405px"><div class="inner"></div>
  <svg viewBox="0 0 48 48" fill="none" stroke="#7cc242" stroke-width="1.8" stroke-linejoin="round"><circle cx="24" cy="8" r="4"/><circle cx="10" cy="12" r="3"/><circle cx="38" cy="12" r="3"/><circle cx="24" cy="30" r="12"/><path d="M12 30h24M24 18v24M17 21c4 6 10 6 14 0M17 39c4-6 10-6 14 0"/></svg>
  <div class="label">Professional Work</div></div>

<div class="why-hex" style="left:253px;top:2605px"><div class="inner"></div>
  <svg viewBox="0 0 48 48" fill="none" stroke="#7cc242" stroke-width="1.8" stroke-linejoin="round"><path d="M24 4 40 10v12c0 11-7 18-16 22C15 40 8 33 8 22V10z"/><path d="M24 9 35 13v9c0 8-5 13-11 16-6-3-11-8-11-16v-9z"/><path d="m18 24 5 5 8-9"/></svg>
  <div class="label">Safety is Our No.1<br>Priority</div></div>
<div class="why-hex" style="left:488px;top:2605px"><div class="inner"></div>
  <svg viewBox="0 0 48 48" fill="none" stroke="#7cc242" stroke-width="1.8" stroke-linejoin="round"><rect x="8" y="4" width="24" height="38" rx="2"/><rect x="12" y="8" width="16" height="8"/><path d="M13 22h3M19 22h3M25 22h3M13 28h3M19 28h3M25 28h3M13 34h3M19 34h3"/><circle cx="36" cy="34" r="7"/><path d="M36 30v8"/></svg>
  <div class="label">Free Estimates</div></div>
<div class="why-hex" style="left:722px;top:2605px"><div class="inner"></div>
  <svg viewBox="0 0 48 48" fill="none" stroke="#7cc242" stroke-width="1.8" stroke-linejoin="round"><path d="M14 8h24v28a4 4 0 0 1-4 4H12"/><path d="M14 8a4 4 0 0 0-4 4v24a4 4 0 0 1-4 4h6"/><path d="M38 8a4 4 0 0 1 4 4h-4"/><path d="M26 14l6 2v5c0 4-3 6-6 7-3-1-6-3-6-7v-5z"/><path d="M18 32h14"/></svg>
  <div class="label">Licensed Arborist<br>on Staff</div></div>

<!-- gallery -->
<h2 class="section-title serif" style="top:3090px;color:var(--heading)">GALLERY</h2>
<div class="gallery-tile" role="img" aria-label="Photo of gloved hands cutting a branch with loppers" style="left:143px;top:3153px;width:217px;height:427px;background:linear-gradient(170deg,#3a3633,#8a4a44 45%,#4f7a30 70%,#6d9e45)"></div>
<div class="gallery-tile" role="img" aria-label="Photo of a worker on a tree trunk above a house roof" style="left:376px;top:3153px;width:448px;height:205px;background:linear-gradient(160deg,#6f8a4c,#7f7566 55%,#9ea3a0)"></div>
<div class="abs" style="left:569px;top:3225px;width:62px;height:62px;border-radius:50%;background:var(--white)"></div>
<svg class="abs" style="left:589px;top:3245px" width="22" height="22" viewBox="0 0 22 22" stroke="#333" stroke-width="2"><path d="M11 4v14M4 11h14"/></svg>
<div class="gallery-tile" role="img" aria-label="Photo of a chainsaw cutting a fallen tree" style="left:840px;top:3153px;width:217px;height:205px;background:linear-gradient(160deg,#5b7a3c,#b8b3a8 50%,#4a4238)"></div>
<div class="gallery-tile" role="img" aria-label="Photo of a climber in a tall birch tree" style="left:376px;top:3376px;width:215px;height:204px;background:linear-gradient(160deg,#8dbb55,#c9d8b0 50%,#6a9a3a)"></div>
<div class="gallery-tile" role="img" aria-label="Photo of an arborist cutting a large limb in a leafy tree" style="left:607px;top:3376px;width:447px;height:204px;background:linear-gradient(160deg,#6aa53a,#3d5a2a 50%,#7fb545)"></div>

<!-- footer -->
<footer>
  <div class="footer-brand"><span class="brand-mark"></span><span class="brand-name">Corvane<br>Tree Care</span></div>

  <h4 class="foot-h serif" style="left:488px">Quick Links</h4>
  <ul class="foot-list" style="left:488px"><li>Home</li><li>About</li><li>Services</li><li>Showcase</li><li>Contact</li></ul>

  <h4 class="foot-h serif" style="left:657px">Resources</h4>
  <ul class="foot-list" style="left:657px"><li>Contact</li><li>Blog</li><li>Info</li><li>Account</li></ul>

  <h4 class="foot-h serif" style="left:816px">Contact Us</h4>
  <div class="contact-item" style="top:3872px">
    <span class="contact-icon"><svg viewBox="0 0 12 12" fill="#fff"><path d="M6 1a3.5 3.5 0 0 0-3.5 3.5C2.5 7.5 6 11 6 11s3.5-3.5 3.5-6.5A3.5 3.5 0 0 0 6 1zm0 5a1.5 1.5 0 1 1 0-3 1.5 1.5 0 0 1 0 3z"/></svg></span>
    <span>123, Lorem ipsum dolor sit<br>amet, consectetur</span>
  </div>
  <div class="contact-item" style="top:3926px">
    <span class="contact-icon"><svg viewBox="0 0 12 12" fill="#fff"><path d="M3 1h2l1 2.5-1.2.8a6 6 0 0 0 2.9 2.9l.8-1.2L11 7v2a1 1 0 0 1-1 1A9 9 0 0 1 2 2a1 1 0 0 1 1-1z"/></svg></span>
    <span style="padding-top:4px">(555) 014 - 7731</span>
  </div>
  <div class="contact-item" style="top:3966px">
    <span class="contact-icon"><svg viewBox="0 0 12 12" fill="#fff"><path d="M1 3h10v6H1z"/><path d="m1 3 5 4 5-4" fill="none" stroke="#7cc242" stroke-width="1"/></svg></span>
    <span style="padding-top:4px">info@corvanetree.com</span>
  </div>

  <div class="foot-line"></div>
  <p class="copyright">© Copyrights 2024 | All Rights Reserved</p>
</footer>

</body>
</html>
```